Lena Corvell Business Card

I need a business card that reflects my current website: itslenacorvell.example and screenshot attached. If we keep the color scheme of the site and sample card below that would be ideal. The business card should include the information on the attached sample cards.

Industry/Entity Type

Business

```html
<!DOCTYPE html>
<html lang="en">
<head>
<meta charset="utf-8">
<title>Lena Corvell Business Card</title>
<link href="https://fonts.googleapis.com/css2?family=Michroma&family=Open+Sans:wght@400;600&display=swap" rel="stylesheet">
<style>
  :root {
    --backdrop: #1c1c1e;
    --card-blue: #1f5fbf;
    --band-deep: #1a4fa3;
    --band-light: #ffffff;
    --accent-yellow: #f4ee1c;
    --text-light: #ffffff;
  }
  * { margin: 0; padding: 0; box-sizing: border-box; }
  html, body {
    width: 1200px;
    height: 900px;
    overflow: hidden;
    background: var(--backdrop);
  }
  .card {
    position: absolute;
    left: 100px;
    top: 164px;
    width: 1000px;
    height: 572px;
    background: var(--card-blue);
    overflow: hidden;
    color: var(--text-light);
  }
  .card__name {
    position: absolute;
    right: 48px;
    top: 52px;
    font-family: "Michroma", sans-serif;
    font-size: 42px;
    letter-spacing: 2px;
    text-transform: uppercase;
  }
  .card__roles {
    position: absolute;
    right: 48px;
    top: 118px;
    font-family: "Open Sans", sans-serif;
    font-size: 20px;
    font-weight: 600;
  }
  .rule {
    position: absolute;
    left: 0;
    width: 100%;
    height: 4px;
    background: var(--accent-yellow);
  }
  .rule--top { top: 158px; }
  .rule--bottom { top: 280px; }
  .band {
    position: absolute;
    left: 0;
    top: 172px;
    width: 100%;
    height: 84px;
    background: linear-gradient(90deg, var(--band-deep) 0%, #8fa9d8 35%, var(--band-light) 62%, var(--band-light) 76%, #6f8fcf 92%, var(--band-deep) 100%);
  }
  .band__shadow {
    position: absolute;
    left: 0;
    top: 256px;
    width: 100%;
    height: 12px;
    background: var(--band-deep);
  }
  .band__signature {
    position: absolute;
    left: 460px;
    top: 190px;
    width: 300px;
    height: 54px;
    background: linear-gradient(90deg, rgba(255,255,255,0.6), #ffffff, rgba(255,255,255,0.6));
  }
  .contact {
    position: absolute;
    right: 52px;
    top: 298px;
    list-style: none;
    text-align: right;
    font-family: "Open Sans", sans-serif;
    font-size: 28px;
    line-height: 40px;
  }
</style>
</head>
<body>
  <section class="card">
    <h1 class="card__name">Lena Corvell</h1>
    <p class="card__roles">Brand Curator I Digital Storyteller I Social Entrprenuer</p>
    <div class="rule rule--top"></div>
    <div class="band"></div>
    <div class="band__shadow"></div>
    <div class="band__signature" role="img" aria-label="Handwritten signature reading i am Lena Corvell"></div>
    <div class="rule rule--bottom"></div>
    <ul class="contact">
      <li>me@lenacorvell.example</li>
      <li>555.010.4821</li>
      <li>@itslenacorvell</li>
      <li>[fb] I [t.] I [ig] @itslenacorvell.example</li>
      <li>www.itslenacorvell.example</li>
    </ul>
  </section>
</body>
</html>
```